Business card design for Summit Wallcrafters required

Our company "Boardwork Ontrack Polishing Venture" needs business cards. Make the business cards be found easily amongst 100 other construction business cards. White background, logo centered and large.

Target Market(s)

Customers or builders who need a drywaller and customers who need a very high quality drywaller.

Industry/Entity Type

Construction

Contact Information for Business Card

The business logo centered and large with "Serving Ridgefall County 15+years" in black Italic, and 2 telephone numbers centered beneath written: Kim / Dale: 403-555-0182, and 403-555-0347 beneath. The business cards will be printed in metal with rounded corners.

Colors
ec1f27

Requirements
Must have
• The selected logo. Must be able to see "BOARDWORK" from a distance. Must stick out from other business cards.

```html
<!DOCTYPE html>
<html lang="en">
<head>
<meta charset="utf-8">
<title>Summit Wallcrafters – Business Cards</title>
<link rel="stylesheet" href="https://fonts.googleapis.com/css2?family=Open+Sans:ital,wght@0,400;0,600;0,700;1,600&display=swap">
<style>
  :root {
    --backdrop: #1c1c1c;
    --card-light: #f4efe2;
    --card-mid: #e9e0c9;
    --card-shade: #dccfb0;
    --brand-red: #ec1f27;
    --gold: #e2a52a;
    --ink: #1d1d1d;
    --rule: #2a2a2a;
  }
  * { margin: 0; padding: 0; box-sizing: border-box; }
  html, body {
    width: 1200px; height: 873px; overflow: hidden;
    background: var(--backdrop);
    font-family: "Open Sans", Arial, sans-serif;
    color: var(--ink);
  }
  .stage {
    position: relative; width: 1200px; height: 873px;
    display: flex; flex-direction: column; align-items: center; justify-content: center; gap: 48px;
  }
  .card {
    position: relative; width: 630px; height: 360px;
    border-radius: 22px; overflow: hidden;
  }
  .card__surface {
    position: absolute; inset: 0;
    background: radial-gradient(ellipse at 40% 35%, var(--card-light) 0%, var(--card-mid) 65%, var(--card-shade) 100%);
  }
  .brand-name {
    position: absolute; left: 0; right: 0;
    text-align: center; white-space: nowrap;
    font-family: "Open Sans", Arial, sans-serif;
    font-weight: 700; color: var(--brand-red); line-height: 1;
  }
  /* front */
  .card--front .brand-name { top: 152px; font-size: 46px; }
  /* back */
  .service-note {
    position: absolute; left: 0; right: 0; top: 22px;
    text-align: center; font-size: 11px; font-style: italic; font-weight: 600;
  }
  .card--back .brand-name { top: 42px; font-size: 32px; }
  .rule { position: absolute; height: 1.5px; background: var(--rule); }
  .rule--logo { left: 140px; right: 140px; top: 96px; }
  .rule--name { left: 190px; right: 34px; top: 206px; }
  .person { position: absolute; left: 40px; top: 192px; }
  .person__name { font-size: 18px; color: var(--gold); font-weight: 400; }
  .person__title { font-size: 12px; font-weight: 700; }
  .website {
    position: absolute; right: 40px; top: 216px;
    font-size: 13px; font-weight: 700;
  }
  .contact-list { position: absolute; left: 40px; top: 262px; list-style: none; }
  .contact-list li {
    display: flex; align-items: center; gap: 12px;
    font-size: 14px; height: 22px;
  }
  .contact-list svg { width: 14px; height: 14px; flex: none; }
</style>
</head>
<body>
<main class="stage">
  <section class="card card--front">
    <div class="card__surface" role="img" aria-label="Cream plaster stucco texture background"></div>
    <p class="brand-name">Summit Wallcrafters</p>
  </section>

  <section class="card card--back">
    <div class="card__surface" role="img" aria-label="Cream plaster stucco texture background"></div>
    <p class="service-note">Serving Ridgefall County 15+years</p>
    <p class="brand-name">Summit Wallcrafters</p>
    <div class="rule rule--logo"></div>

    <div class="person">
      <p class="person__name">Marla Fenwick</p>
      <p class="person__title">Bank Rep Officer</p>
    </div>
    <div class="rule rule--name"></div>
    <p class="website">www.summitwallcrafters.com</p>

    <ul class="contact-list">
      <li>
        <svg viewBox="0 0 14 14"><circle cx="7" cy="7" r="7" fill="var(--gold)"/><path d="M4.5 3.8c.4-.4 1-.4 1.3 0l.8 1c.2.3.2.7-.1 1l-.4.4c.4.8 1 1.4 1.8 1.8l.4-.4c.3-.3.7-.3 1-.1l1 .8c.4.3.4.9 0 1.3-.9.9-2.5.7-4-.8S3.6 4.7 4.5 3.8z" fill="#fff"/></svg>
        Kim / Dale: 403-555-0182
      </li>
      <li>
        <svg viewBox="0 0 14 14"><circle cx="7" cy="7" r="7" fill="var(--gold)"/><path d="M4.5 3.8c.4-.4 1-.4 1.3 0l.8 1c.2.3.2.7-.1 1l-.4.4c.4.8 1 1.4 1.8 1.8l.4-.4c.3-.3.7-.3 1-.1l1 .8c.4.3.4.9 0 1.3-.9.9-2.5.7-4-.8S3.6 4.7 4.5 3.8z" fill="#fff"/></svg>
        403-555-0347
      </li>
      <li>
        <svg viewBox="0 0 14 14"><circle cx="7" cy="7" r="7" fill="var(--gold)"/><rect x="3.5" y="4.5" width="7" height="5" fill="none" stroke="#fff" stroke-width="1"/><path d="M3.5 4.5 7 7.3l3.5-2.8" fill="none" stroke="#fff" stroke-width="1"/></svg>
        marla.fenwick@summitwallcrafters.com
      </li>
      <li>
        <svg viewBox="0 0 14 14"><circle cx="7" cy="7" r="7" fill="var(--gold)"/><path d="M7 3a2.5 2.5 0 0 0-2.5 2.5C4.5 7.5 7 11 7 11s2.5-3.5 2.5-5.5A2.5 2.5 0 0 0 7 3z" fill="#fff"/><circle cx="7" cy="5.5" r="0.9" fill="var(--gold)"/></svg>
        418 Elm Ave. Garrison, SD 57099
      </li>
    </ul>
  </section>
</main>
</body>
</html>
```